Buch-/E-Book-Cover für Ausbildung und Weiterbildung von angehenden Sommeliers und Connaisseurs in der Spirituosenbranche
Zielgruppe
Ausbildung und Weiterbildung von angehenden Sommeliers und Connaisseurs in der Spirituosenbranche. Zielgruppe sind die Teilnehmer der genannten Kurse, Interessierte, Brenner und Gastronomen.
Aufgabenstellung
Klassisches, edles Design, klares Design, keine Bilder, Typografie steht im Vordergrund. Typografie in Relief.
A4
Vom Stil wie die angehängte Datei
Buchtitel: Kernwasser (groß) - verschnörkelt -
Hintergrund - Blautöne
Schrift: Titel Silber Untertitel: grau
Unterüberschrift: Kultur und Genuss
Autoren: Lehmkuhl • Wittrock
Buchrücken: Oben: Lehmkuhl Wittrock - Quer: Kernwasser - Unten: Amber Vessels

```html
<!DOCTYPE html>
<html lang="de">
<head>
<meta charset="utf-8">
<title>Kernwasser – Kultur und Genuss</title>
<link rel="stylesheet" href="https://fonts.googleapis.com/css2?family=Gelasio:wght@400&family=Yellowtail&family=Kaushan+Script&display=block">
<style>
  :root {
    --navy: #0c2e4d;
    --spine-rule: #05101c;
    --silver: #cbcbcb;
    --grey: #9a9a9a;
    --spine-grey: #a2a2a2;
    --script: "Yellowtail", "Kaushan Script", "Brush Script MT", "Segoe Script", cursive;
  }
  * { margin: 0; padding: 0; box-sizing: border-box; }
  html, body {
    width: 979px;
    height: 1200px;
    overflow: hidden;
    background: var(--navy);
  }
  .cover {
    position: relative;
    width: 979px;
    height: 1200px;
    background: var(--navy);
    font-family: "Gelasio", Georgia, serif;
  }
  .spine {
    position: absolute;
    left: 0;
    top: 0;
    width: 124px;
    height: 1200px;
    overflow: hidden;
  }
  .spine-rule {
    position: absolute;
    left: 124px;
    top: 2px;
    width: 4px;
    height: 1196px;
    background: var(--spine-rule);
  }
  .spine-authors,
  .spine-publisher {
    position: absolute;
    left: 0;
    width: 124px;
    text-align: center;
    color: var(--spine-grey);
    font-size: 24px;
    line-height: 36px;
    white-space: nowrap;
  }
  .spine-authors { top: 20px; }
  .spine-publisher { top: 1104px; }
  .spine-title {
    position: absolute;
    left: 62px;
    top: 575px;
    transform: translate(-50%, -50%) rotate(-90deg);
    font-family: var(--script);
    font-weight: 400;
    font-size: 80px;
    line-height: 1;
    color: var(--spine-grey);
    white-space: nowrap;
  }
  .front {
    position: absolute;
    left: 128px;
    top: 0;
    width: 851px;
    height: 1200px;
    text-align: center;
  }
  .book-title {
    position: absolute;
    left: 0;
    right: 0;
    top: 405px;
    font-family: var(--script);
    font-weight: 400;
    font-size: 150px;
    line-height: 1;
    white-space: nowrap;
    color: var(--silver);
    text-shadow: 1px 1px 0 #8f8f8f, 2px 3px 3px rgba(0,0,0,0.35), -1px -1px 0 rgba(255,255,255,0.15);
  }
  .book-subtitle {
    position: absolute;
    left: 0;
    right: 0;
    top: 585px;
    font-size: 76px;
    font-weight: 400;
    line-height: 1;
    color: var(--grey);
  }
  .book-authors {
    position: absolute;
    left: 0;
    right: 0;
    top: 1105px;
    font-size: 50px;
    line-height: 1;
    color: var(--grey);
  }
</style>
</head>
<body>
  <div class="cover">
    <aside class="spine">
      <p class="spine-authors">Lehmkuhl<br>Wittrock</p>
      <p class="spine-title">Kernwasser</p>
      <p class="spine-publisher">Amber<br>Vessels</p>
    </aside>
    <div class="spine-rule"></div>
    <section class="front">
      <h1 class="book-title">Kernwasser</h1>
      <h2 class="book-subtitle">Kultur und Genuss</h2>
      <p class="book-authors">Lehmkuhl • Wittrock</p>
    </section>
  </div>
</body>
</html>
```